Web Design Project

We need the homepage and 7 interior pages designed as described below - design only:

Main Page
We like this template: http://www.layoutbarn.example/demo/52917.html

We also want a login dropdown similar to http://www.vortelle.example

We want the main page to be luxurious and sleek. We are a limo company that is dedicated to good service and creating an experience, and our front page should strongly reflect that. We do not want a very busy front page.

The main page should do primary things:

1. Make Reservations: We really like rideharbor.example for this aspect of the site. That being said, rideharbor is NOT the type of company we are.
2. Inform the customer of our most popular packages and give a sense of our professionalism and luxurious service.
3. There should be an area for a customer login
4. Menu should include the following: Home, Who We Are, Our Fleet, Custom Packages,
Testimonials, Book Your Ride!

For a starting point, we like this template http://www.layoutbarn.example/demo/52917.html

Rather than "start up, integrate, develop" we could have 3 of the more popular packages (or categories of packages). The bottom part would be fine. We could have a chirpline feed, welcome, and our core principles. The one big change would be the addition of a "booking" area right smack in the middle of the page, where a customer could enter in trip data and see if the date was available.

-

About Us - Secondary Page
We like this ABOUT page template: http://www.layoutbarn.example/demo/63824.html

This is a really important page that people overlook, yet it is the most viewed page of a website after the homepage. We have come up with a bit of text to go on the about us page:

Who We Are: Velvet Cars was founded on the core principle that every limo ride starts with personalized service from the instant you book your ride and continues after you step out of the car. You and your party are more than just our customers. We consider knowing your name and providing you with your choice of snacks and periodicals in the car just a few of the integral elements of the limousine experience. We are striving to revolutionize the limousine industry by creating a personal, friendly, timely, and professional experience. Velvet Cars combines current technology and a modern fleet with good old-fashioned service to deliver you a personalized, luxury experience. We cater to every event, from business travel to proms and wedding, and everything in between.

We do all of this while maintaining competitive pricing to our peers.

Have a taste of high society...

-

Custom Packages - Secondary Page

This page will contain descriptions of the packages that we offer: Wedding, Prom, Business, etc. - there should be a thumbnail of each package with a description next to it. When you click on a thumbnail it will bring you to a detailed page of that particular package.

-

Custom Packages Interior Page - Secondary Page

In depth look at that particular package - for example, weddings - shows that we offer complimentary champagne, Just married sign, etc.

-

Fleet Page - Secondary Page

This page can be fairly basic. It will include photos of the vehicles along with descriptions and number of passengers, etc.

-

Testimonials Page - Secondary Page

This page will have testimonials from customers. We don't want a big block of text, but rather small testimonials that will expand within the page when you click on a "+" symbol. We like the way it looks when the testimonials are enclosed within a speech bubble image - still professional and classy, not cheesy.

-

Book your ride! - Secondary Page

This page will have a form on it - the same as the form on the homepage, where people can enter in information to check the availability of vehicles. We also want basic contact information on this page as well in case people want to call directly or e-mail.

Requirements
Must have
• - Book your reservation form on homepage
- Sleek, elegant feel
- Chirpline feed

```html
<!DOCTYPE html>
<html lang="en">
<head>
<meta charset="utf-8">
<title>Velvet Cars</title>
<link href="https://fonts.googleapis.com/css2?family=PT+Sans:ital,wght@0,400;0,700;1,400&family=PT+Sans+Narrow:wght@400;700&display=swap" rel="stylesheet">
<style>
:root{
  --navy:#13297c;
  --navy-deep:#0d1f66;
  --royal:#1c4fb0;
  --sky:#5fb6f0;
  --sky-light:#b9def8;
  --tile:#2d7fd0;
  --ink:#1d1d1d;
  --muted:#6a6a6a;
  --line:#d9d9d9;
  --panel:#ffffff;
  --soft:#f1f1f1;
  --head:#0f2b7a;
}
*{box-sizing:border-box;margin:0;padding:0}
html,body{width:1104px;height:1200px;overflow:hidden}
body{
  position:relative;
  font-family:"PT Sans",sans-serif;color:var(--ink);
  background:radial-gradient(ellipse 700px 260px at 250px 40px,#2a6ad0 0%,transparent 70%),linear-gradient(180deg,#1a3c9a 0%,var(--navy) 22%,var(--navy-deep) 100%);
}
.abs{position:absolute}
.brand{left:86px;top:52px;color:#fff;display:flex;align-items:center;gap:10px}
.brand__mark{width:14px;height:14px;border-radius:50%;background:#fff}
.brand__name{font-size:28px;font-weight:400;letter-spacing:0}
.call{right:48px;top:66px;color:#fff;font-size:19px;display:flex;align-items:center;gap:8px}
.nav{left:83px;top:111px;width:937px;height:84px;border-radius:6px;background:#dfe3ea;padding:4px;box-shadow:0 0 0 2px #5c79c4 inset}
.nav ul{list-style:none;display:flex;height:100%;background:linear-gradient(#fbfbfb,#ececec);border-radius:3px}
.nav li{display:flex;flex-direction:column;align-items:center;justify-content:flex-end;padding-bottom:10px;font-size:13px;color:#333;border-right:1px solid #cfcfcf;gap:10px}
.nav li:last-child{border-right:0}
.nav li.is-active{background:#e6e6e6}
.nav svg{height:30px}
.main{left:83px;top:209px;width:937px;height:818px;background:var(--panel);border:2px solid #fff}
.hero{position:absolute;left:0;top:0;width:933px;height:341px;background:linear-gradient(160deg,#2b8ee3 0%,#7cc6f5 40%,#bfe1f8 70%,#5db1ee 100%)}
.hero__title{position:absolute;left:52px;top:36px;color:#fff;font-size:26px;font-weight:400}
.hero__rule{position:absolute;left:52px;top:82px;width:508px;border-top:1px dotted #fff}
.hero__text{position:absolute;left:52px;top:103px;width:512px;font-size:12px;line-height:21px}
.hero__photo{position:absolute;left:0;top:204px;width:590px;height:172px;border-radius:80px 40px 10px 10px;background:linear-gradient(180deg,#f7f7f7,#d6d9de)}
.booking{position:absolute;left:615px;top:17px;width:305px;height:326px;background:linear-gradient(#e8f3fc,#b8daf5);border:4px solid #cfe5f7;border-radius:4px}
.booking h2{font-weight:400;font-size:22px;color:#1b2b55;display:flex;align-items:center;gap:10px;padding:18px 0 0 18px;height:64px;border-bottom:1px solid #d3e6f6}
.field{display:flex;align-items:center;position:absolute;left:26px;font-size:11px;color:#333}
.field label{width:62px}
.input{height:24px;background:#fff;border:1px solid #c9d4df;font-style:italic;font-size:11px;color:#444;padding:0 10px;display:flex;align-items:center;justify-content:space-between}
.caret{width:0;height:0;border-left:4px solid transparent;border-right:4px solid transparent;border-top:5px solid #666}
.btn-reserve{position:absolute;left:669px;top:314px;width:210px;height:45px;border-radius:23px;background:linear-gradient(#3158b8,#13297c);color:#fff;font-size:17px;display:flex;align-items:center;justify-content:center;box-shadow:0 6px 8px rgba(0,0,0,.25)}
.col{position:absolute;top:433px;width:290px}
.col h3{font-family:"PT Sans Narrow",sans-serif;font-weight:700;font-size:24px;color:var(--head);margin-bottom:22px}
.item{display:flex;gap:15px;height:97px}
.thumb{width:75px;height:78px;flex:none}
.tile{background:var(--tile);color:#fff;text-align:center;font-family:"PT Sans Narrow",sans-serif}
.tile b{display:block;font-size:30px;line-height:36px;color:#b9dcff}
.tile span{font-size:23px}
.photo{background:linear-gradient(#f4f4f4,#cfd3d8)}
.quote{background:#eee;color:#555;font-family:"PT Sans Narrow",sans-serif;font-size:14px;display:flex;flex-direction:column;justify-content:center;align-items:center;line-height:20px}
.item p{font-size:12px;line-height:17.5px;color:#333}
.item a{display:block;font-size:12px;color:#1b3f9e;text-decoration:underline;margin-top:6px}
.viewall{height:22px;background:var(--soft);text-align:right;padding-right:12px;font-family:"PT Sans Narrow",sans-serif;font-size:13px;line-height:22px;margin-top:-6px}
.login{left:83px;top:1027px;width:939px;height:90px;background:linear-gradient(#f7f7f7,#e9e9e9);display:flex;align-items:center}
.login h4{font-weight:400;font-size:26px;color:#333;margin-left:14px;width:205px}
.login .sep{width:1px;height:70px;background:#d3d3d3;margin-right:16px}
.login label{font-style:italic;font-size:12px;color:#444;margin-right:10px}
.login .box{width:150px;height:28px;background:#fff;border:1px solid #cfcfcf;margin-right:28px}
.btn-sign{width:76px;height:29px;border-radius:15px;background:linear-gradient(#3158b8,#13297c);color:#fff;font-size:13px;display:flex;align-items:center;justify-content:center;margin-left:6px}
.footer-nav{left:90px;top:1139px;color:#fff;font-size:11px}
.footer-nav span{margin:0 6px}
.copy{left:90px;top:1169px;color:#fff;font-size:11px}
.social{right:50px;top:1148px;display:flex;gap:8px;color:#fff;font-size:10px}
.social div{display:flex;align-items:center;gap:4px}
.social i{width:10px;height:10px;border-radius:50%;background:#fff;display:block}
</style>
</head>
<body>
<header>
  <div class="abs brand"><span class="brand__mark"></span><span class="brand__name">Velvet Cars</span></div>
  <div class="abs call">
    <svg width="24" height="22" viewBox="0 0 24 22"><path d="M3 8c0-4 18-4 18 0l-3 3-3-2V6H9v3l-3 2z" fill="#cfe3ff"/><rect x="6" y="12" width="12" height="8" rx="2" fill="#cfe3ff"/></svg>
    Call us : 555 018 2740
  </div>
</header>
<nav class="abs nav">
  <ul>
    <li class="is-active" style="width:105px"><svg viewBox="0 0 30 30" width="30"><path d="M3 15 15 4l12 11" stroke="#666" stroke-width="3" fill="none"/><rect x="7" y="14" width="16" height="13" fill="#ddd" stroke="#777"/><rect x="12" y="17" width="6" height="5" fill="#3a7be0"/></svg>HOME</li>
    <li style="width:131px"><svg viewBox="0 0 30 30" width="30"><circle cx="15" cy="9" r="6" fill="#e08a4a"/><path d="M4 29c0-9 5-12 11-12s11 3 11 12z" fill="#2c4fa3"/><path d="M15 17l-2 6 2 5 2-5z" fill="#d22"/></svg>WHO WE ARE</li>
    <li style="width:115px"><svg viewBox="0 0 54 30" width="54"><path d="M2 18h50v6H2zM12 18l5-6h20l5 6z" fill="#222"/><circle cx="12" cy="25" r="3" fill="#555"/><circle cx="42" cy="25" r="3" fill="#555"/></svg>OUR FLEET</li>
    <li style="width:167px"><svg viewBox="0 0 30 30" width="30"><text x="15" y="26" text-anchor="middle" font-size="28" font-weight="700" fill="#2a9b3a" font-family="PT Sans,sans-serif">$</text></svg>CUSTOM PACKAGES</li>
    <li style="width:135px"><svg viewBox="0 0 30 30" width="30"><rect x="5" y="3" width="20" height="25" fill="#f4f4f4" stroke="#888"/><path d="M9 10h12M9 15h12M9 20h8" stroke="#999"/></svg>TESTIMONIALS</li>
    <li style="width:155px"><svg viewBox="0 0 30 30" width="30"><rect x="8" y="3" width="14" height="25" rx="7" fill="#f7f7f7" stroke="#999"/><path d="M15 3v9" stroke="#999"/></svg>BOOK YOUR RIDE!</li>
    <li style="width:127px"><svg viewBox="0 0 40 30" width="40"><path d="M4 10c0-7 32-7 32 0l-5 4-4-3V8H13v3l-4 3z" fill="#222"/><rect x="8" y="15" width="24" height="12" rx="2" fill="#333"/></svg>CONTACT</li>
  </ul>
</nav>
<main class="abs main">
  <section class="hero">
    <h1 class="hero__title">WELCOME TO VELVET CARS</h1>
    <div class="hero__rule"></div>
    <p class="hero__text">Neque porro quisquam est, qui dolorem ipsum quia dolor sit amet, consectetur, adipisci velit, sed quia non numquam eius modi tempora incidunt ut labore et dolore magnam aliquam quaerat voluptatem. Ut enim ad minima veniam, quis nostrum exercitationem ullam corporis suscipit laboriosam, nisi ut aliquid ex ea commodi consequatur.</p>
    <div class="hero__photo" role="img" aria-label="Photo of a white stretch limousine"></div>
    <form class="booking">
      <h2><svg width="34" height="30" viewBox="0 0 34 30"><rect x="4" y="6" width="26" height="22" fill="#fff" stroke="#5b7fb5" transform="rotate(-10 17 17)"/><path d="M8 6h20" stroke="#345" stroke-width="3" stroke-dasharray="2 2" transform="rotate(-10 17 17)"/></svg>Make reservations</h2>
      <div class="field" style="top:86px"><label>For :</label><div class="input" style="width:130px">One way<span class="caret"></span></div></div>
      <div class="field" style="top:128px"><label>From :</label><div class="input" style="width:210px">Place, City, Zip</div></div>
      <div class="field" style="top:170px"><label>To :</label><div class="input" style="width:210px">Place, City, Zip</div></div>
      <div class="field" style="top:212px"><label>Occasion :</label><div class="input" style="width:210px">Wedding<span class="caret"></span></div></div>
      <div class="field" style="top:254px"><label>Date :</label>
        <div class="input" style="width:68px">Date<span class="caret"></span></div>
        <div class="input" style="width:68px;margin-left:3px">Month<span class="caret"></span></div>
        <div class="input" style="width:68px;margin-left:3px">Year<span class="caret"></span></div>
      </div>
    </form>
    <div class="btn-reserve">MAKE RESERVATION</div>
  </section>

  <section class="col" style="left:8px">
    <h3>POPULAR PACKAGES</h3>
    <div class="item"><div class="thumb tile"><b>1</b><span>$00.00</span></div><div><p>Neque porro quisquam est, qui dolor em ipsum quia dolor sit amet, consectetur, adipisci velit, sed.</p><a>View more</a></div></div>
    <div class="item"><div class="thumb tile"><b>1</b><span>$00.00</span></div><div><p>Neque porro quisquam est, qui dolor em ipsum quia dolor sit amet, consectetur, adipisci velit, sed.</p><a>View more</a></div></div>
    <div class="item"><div class="thumb tile"><b>1</b><span>$00.00</span></div><div><p>Neque porro quisquam est, qui dolor em ipsum quia dolor sit amet, consectetur, adipisci velit, sed.</p><a>View more</a></div></div>
    <div class="viewall" style="width:284px">VIEW ALL</div>
  </section>

  <section class="col" style="left:326px">
    <h3>OUR SERVICES</h3>
    <div class="item"><div class="thumb photo" role="img" aria-label="Photo of a white limousine"></div><div><p>Neque porro quisquam est, qui dolor em ipsum quia dolor sit amet, consectetur, adipisci velit, sed.</p><a>View more</a></div></div>
    <div class="item"><div class="thumb photo" role="img" aria-label="Photo of a chauffeur beside a black car"></div><div><p>Neque porro quisquam est, qui dolor em ipsum quia dolor sit amet, consectetur, adipisci velit, sed.</p><a>View more</a></div></div>
    <div class="item"><div class="thumb photo" role="img" aria-label="Photo of a black sedan"></div><div><p>Neque porro quisquam est, qui dolor em ipsum quia dolor sit amet, consectetur, adipisci velit, sed.</p><a>View more</a></div></div>
    <div class="viewall" style="width:278px">VIEW ALL</div>
  </section>

  <section class="col" style="left:635px">
    <h3>TESTIMONIALS</h3>
    <div class="item"><div class="thumb quote">John Doe<br>Cityname</div><div><p>Neque porro quisquam est, qui dolor em ipsum quia dolor sit amet, consectetur, adipisci velit, sed.</p><a>View more</a></div></div>
    <div class="item"><div class="thumb quote">John Doe<br>Cityname</div><div><p>Neque porro quisquam est, qui dolor em ipsum quia dolor sit amet, consectetur, adipisci velit, sed.</p><a>View more</a></div></div>
    <div class="item"><div class="thumb quote">John Doe<br>Cityname</div><div><p>Neque porro quisquam est, qui dolor em ipsum quia dolor sit amet, consectetur, adipisci velit, sed.</p><a>View more</a></div></div>
    <div class="viewall" style="width:284px">VIEW ALL</div>
  </section>
</main>

<section class="abs login">
  <svg style="margin-left:40px" width="40" height="50" viewBox="0 0 40 50"><path d="M10 22V13a10 10 0 0 1 20 0v9" stroke="#888" stroke-width="4" fill="none"/><rect x="5" y="22" width="30" height="26" rx="3" fill="#b5b5b5"/></svg>
  <h4>MEMBER LOGIN</h4>
  <div class="sep"></div>
  <label>Username :</label><div class="box"></div>
  <label>Password :</label><div class="box"></div>
  <div class="btn-sign">SIGN IN</div>
</section>

<footer>
  <div class="abs footer-nav">Home<span>|</span>Who We Are<span>|</span>Our Fleet<span>|</span>Custom Packages<span>|</span>Testimonials<span>|</span>Book Your Ride!<span>|</span>Contact</div>
  <div class="abs copy">Copyright © 2012 www.velvetcars.example &nbsp;&nbsp;All rights reserved.</div>
  <div class="abs social"><div><i></i>Friendwall</div><div><i></i>Chirpline</div><div><i></i>Searchly</div></div>
</footer>
</body>
</html>
```